Birchmoor Yard Care_2015 New Cards_V1

We need an enhanced business card from what we have today. We are a Landscaping company and we have an existing Logo and text info that we would like to include.
Text to include:
In business for over 20 years,Fully Insured, Weekly Lawn Maintenance, Spring & Fall Clean-up, Todd Pierson, 203-555-0147, www.birchmooryardcarect.example, Visit our Website for additional Lawn Care Services or email directly at TODD@BIRCHMOORYARDCARE.EXAMPLE, We appreciate your business.
We want full color background and we will want to take this design and work with a printer that does high graphic silk screen cards. The colors we have thought about are Black, with our Green Logo, with Gold Text...we are open to different colors, we just want the card to wow!

Target Market(s)

Lawn Care Maintenance

Industry/Entity Type

Lawn Care

Contact Information for Business Card

Text to include:
In business for over 20 years, Fully Insured, Weekly Lawn Maintenance, Spring & Fall Clean-up, Todd Pierson, 203-555-0147, www.birchmooryardcarect.example, Visit our Website for additional Lawn Care Services or email directly at TODD@BIRCHMOORYARDCARE.EXAMPLE, We appreciate your business.

Requirements
Must have
• Logo, text details about how to reach us, standard size business cards that go horizontal.
Nice to have
• background colors, background designs, raised embossed lettering, rounded corners(2 or 4),

```html
<!DOCTYPE html>
<html lang="en">
<head>
<meta charset="utf-8">
<title>Birchmoor Yard Care – Business Card</title>
<link rel="stylesheet" href="https://fonts.googleapis.com/css2?family=Arimo:wght@400;700&family=Open+Sans:wght@400;500;600&display=swap">
<style>
  :root {
    --backdrop: #a3adaa;
    --front-green: #1f311f;
    --back-green: #07350f;
    --logo-green: #1d3a1f;
    --paper: #ffffff;
    --soft-paper: rgba(255,255,255,0.82);
    --sky-top: #5b8fc4;
    --sky-mid: #8fb3d6;
    --blossom: #eef0f2;
  }
  * { margin: 0; padding: 0; box-sizing: border-box; }
  html, body {
    width: 1189px; height: 1200px; overflow: hidden;
    background: var(--backdrop);
  }
  .card {
    position: absolute;
    left: 129px;
    width: 914px;
    height: 520px;
    border-radius: 46px;
    overflow: hidden;
    box-shadow: 0 4px 10px rgba(0,0,0,0.35);
  }
  .card--front { top: 41px; background: var(--front-green); }
  .card--back { top: 619px; background: var(--back-green); }

  .front-header {
    position: absolute; left: 0; top: 0;
    width: 100%; height: 259px;
    background: var(--paper);
  }
  .front-photo { position: absolute; left: 0; top: 0; }

  .brand-name {
    position: absolute;
    left: 460px; width: 420px; top: 92px;
    text-align: center;
    font-family: "Arimo", sans-serif;
    font-weight: 700;
    font-size: 34px;
    letter-spacing: 3px;
    color: var(--logo-green);
    text-transform: uppercase;
    line-height: 1.3;
  }
  .person-name {
    position: absolute;
    right: 53px; top: 301px;
    font-family: "Arimo", sans-serif;
    font-weight: 700;
    font-size: 38px;
    letter-spacing: 1px;
    color: var(--paper);
  }
  .contact-list { list-style: none; }
  .contact-item {
    position: absolute;
    right: 53px;
    display: flex; align-items: center; gap: 16px;
    font-family: "Arimo", sans-serif;
    font-size: 24px;
    color: var(--paper);
    white-space: nowrap;
  }
  .contact-item--phone { top: 396px; }
  .contact-item--email { top: 435px; }
  .contact-item--web { top: 473px; }
  .contact-icon { width: 14px; height: 14px; flex: none; }

  .services-title {
    position: absolute; left: 44px; top: 34px;
    font-family: "Open Sans", sans-serif;
    font-weight: 500;
    font-size: 42px;
    color: var(--paper);
  }
  .services-list { list-style: none; }
  .service {
    position: absolute; left: 44px;
    display: flex; align-items: center;
    font-family: "Open Sans", sans-serif;
    font-size: 27px;
    color: var(--paper);
    transform: translateY(-50%);
    white-space: nowrap;
  }
  .service-star { width: 18px; height: 18px; margin-right: 29px; flex: none; }

  .company-facts {
    position: absolute;
    right: 44px; top: 300px;
    width: 330px;
    text-align: right;
    font-family: "Open Sans", sans-serif;
    color: var(--soft-paper);
  }
  .fact {
    font-size: 22px;
    font-weight: 600;
    line-height: 1.45;
  }
  .thanks {
    margin-top: 22px;
    font-size: 20px;
    font-style: italic;
    color: var(--paper);
  }
</style>
</head>
<body>

<section class="card card--front">
  <div class="front-header"></div>
  <svg class="front-photo" width="914" height="520" viewBox="0 0 914 520" role="img" aria-label="Photo of white cherry blossoms against a blue sky">
    <defs>
      <linearGradient id="blossomTone" x1="0" y1="0" x2="1" y2="1">
        <stop offset="0" stop-color="#5b8fc4"/>
        <stop offset="0.45" stop-color="#8fb3d6"/>
        <stop offset="0.75" stop-color="#e9ecef"/>
        <stop offset="1" stop-color="#d9d4cf"/>
      </linearGradient>
    </defs>
    <path d="M0 0 H332 Q462 260 332 520 H0 Z" fill="url(#blossomTone)"/>
  </svg>

  <div class="brand-name">Birchmoor<br>Yard Care</div>

  <h1 class="person-name">Todd Pierson</h1>

  <ul class="contact-list">
    <li class="contact-item contact-item--phone">
      <span>203-555-0147</span>
      <svg class="contact-icon" viewBox="0 0 14 14" aria-hidden="true">
        <rect width="14" height="14" rx="2" fill="#fff"/>
        <path d="M4 3.5 L6 3.5 L6.5 5.5 L5.5 6.2 Q6.5 8 7.8 8.6 L8.6 7.6 L10.5 8.2 L10.5 10.2 Q6 10.5 4 3.5 Z" fill="#1f311f"/>
      </svg>
    </li>
    <li class="contact-item contact-item--email">
      <span>todd@birchmooryardcare.example</span>
      <svg class="contact-icon" viewBox="0 0 14 14" aria-hidden="true">
        <rect width="14" height="14" rx="2" fill="#fff"/>
        <rect x="3" y="4.5" width="8" height="5" fill="none" stroke="#1f311f" stroke-width="1.2"/>
        <path d="M3 4.5 L7 7.5 L11 4.5" fill="none" stroke="#1f311f" stroke-width="1.2"/>
      </svg>
    </li>
    <li class="contact-item contact-item--web">
      <span>www.birchmooryardcarect.example</span>
      <svg class="contact-icon" viewBox="0 0 14 14" aria-hidden="true">
        <rect width="14" height="14" rx="2" fill="#fff"/>
        <circle cx="7" cy="7" r="3.6" fill="none" stroke="#1f311f" stroke-width="1.2"/>
        <path d="M3.4 7 H10.6 M7 3.4 V10.6" stroke="#1f311f" stroke-width="1"/>
      </svg>
    </li>
  </ul>
</section>

<section class="card card--back">
  <h2 class="services-title">Services</h2>
  <ul class="services-list">
    <li class="service" style="top:133px"><svg class="service-star" viewBox="0 0 20 20" aria-hidden="true"><path d="M10 1 L12.6 7 L19 7.4 L14 11.6 L15.6 18 L10 14.5 L4.4 18 L6 11.6 L1 7.4 L7.4 7 Z" fill="#fff"/></svg>Weekly Mowing</li>
    <li class="service" style="top:188px"><svg class="service-star" viewBox="0 0 20 20" aria-hidden="true"><path d="M10 1 L12.6 7 L19 7.4 L14 11.6 L15.6 18 L10 14.5 L4.4 18 L6 11.6 L1 7.4 L7.4 7 Z" fill="#fff"/></svg>Lawn Maintenance</li>
    <li class="service" style="top:240px"><svg class="service-star" viewBox="0 0 20 20" aria-hidden="true"><path d="M10 1 L12.6 7 L19 7.4 L14 11.6 L15.6 18 L10 14.5 L4.4 18 L6 11.6 L1 7.4 L7.4 7 Z" fill="#fff"/></svg>Mulching of Flower/Plant Beds</li>
    <li class="service" style="top:293px"><svg class="service-star" viewBox="0 0 20 20" aria-hidden="true"><path d="M10 1 L12.6 7 L19 7.4 L14 11.6 L15.6 18 L10 14.5 L4.4 18 L6 11.6 L1 7.4 L7.4 7 Z" fill="#fff"/></svg>Edging</li>
    <li class="service" style="top:346px"><svg class="service-star" viewBox="0 0 20 20" aria-hidden="true"><path d="M10 1 L12.6 7 L19 7.4 L14 11.6 L15.6 18 L10 14.5 L4.4 18 L6 11.6 L1 7.4 L7.4 7 Z" fill="#fff"/></svg>Hedge &amp; Shrub Trimming</li>
    <li class="service" style="top:399px"><svg class="service-star" viewBox="0 0 20 20" aria-hidden="true"><path d="M10 1 L12.6 7 L19 7.4 L14 11.6 L15.6 18 L10 14.5 L4.4 18 L6 11.6 L1 7.4 L7.4 7 Z" fill="#fff"/></svg>Tree &amp; Shrub Plantings</li>
    <li class="service" style="top:453px"><svg class="service-star" viewBox="0 0 20 20" aria-hidden="true"><path d="M10 1 L12.6 7 L19 7.4 L14 11.6 L15.6 18 L10 14.5 L4.4 18 L6 11.6 L1 7.4 L7.4 7 Z" fill="#fff"/></svg>Light Tree Work</li>
  </ul>

  <div class="company-facts">
    <p class="fact">Spring &amp; Fall Clean-up</p>
    <p class="fact">In business for over 20 years</p>
    <p class="fact">Fully Insured</p>
    <p class="thanks">We appreciate your business.</p>
  </div>
</section>

</body>
</html>
```